Design a Brochure for Tidal Crate Supplies

We're in need of a product packaging brochure. I've a brochure we currently already have for a different company as inspiration. This brochure should have a similar lay-out. It's a brochure for packaging Materials such as plastic PET bottles, caps, kraft pouches used for food and beverage filling.

1: Front page (I've attached our banner & company logo you can work off, but feel free to spice it up further)
2: Table of content (look at the categories file I've attached to see which categories should be included)
3: Category front page (please make a pitch for this based on 'syrup bottles)
4: Product page (I've included a sketch with what the lay-out should look like as well as an thumbnail of a bottle to use in your pitch)
5: Contact page (www.tidalcratesupplies.example take contact details from there)

Please use your own creativity and surprise me.

UPDATE:

- New categories have been added, please use these ones
- New Bottle thumbnail has bee nadded, please use this one too!

Inspiration for the 'product page' has been added. Our brochure does not incorporate that much information, but this is what a typical page of a product brochure in our industry looks like.

```html
<!DOCTYPE html>
<html lang="en">
<head>
<meta charset="utf-8">
<title>Tidal Crate Supplies – Packaging Brochure</title>
<link href="https://fonts.googleapis.com/css2?family=Arimo:wght@400;700&display=swap" rel="stylesheet">
<style>
  :root {
    --green-dark: #4f8f1c;
    --green: #6aab2a;
    --green-light: #9fcc4a;
    --cream: #f7f8ec;
    --cream-deep: #e6efc8;
    --ink: #3b3b3b;
    --backdrop: #cfcfcf;
    --white: #ffffff;
  }
  * { box-sizing: border-box; margin: 0; padding: 0; }
  html, body { width: 1200px; height: 4000px; overflow: hidden; }
  body {
    background: var(--backdrop);
    font-family: "Arimo", Arial, sans-serif;
    color: var(--ink);
  }
  .sheet-slot {
    position: relative;
    width: 1200px;
    height: 800px;
  }
  .page {
    position: absolute;
    left: 350px;
    top: 46px;
    width: 500px;
    height: 707px;
    overflow: hidden;
    box-shadow: 0 6px 18px rgba(0,0,0,.25);
  }
  .page--light { background: radial-gradient(ellipse at 70% 30%, var(--white) 0%, var(--cream) 55%, var(--cream-deep) 100%); }
  .page--green { background: linear-gradient(160deg, var(--green-light) 0%, var(--green) 55%, var(--green-dark) 100%); }
  .band { position: absolute; left: 0; width: 500px; display: block; }
  .band--top { top: 0; }
  .band--bottom { bottom: 0; }
  .folio { position: absolute; left: 34px; bottom: 24px; color: var(--white); font-size: 13px; }

  /* cover */
  .brand { position: absolute; left: 40px; top: 70px; display: flex; align-items: center; gap: 10px; }
  .brand__dot { width: 22px; height: 22px; border-radius: 50%; background: var(--green); }
  .brand__name { font-size: 20px; font-weight: 700; color: var(--green-dark); }
  .brand__url { position: absolute; left: 72px; top: 104px; font-size: 9px; color: var(--green-dark); }
  .art { position: absolute; }
  .art--sky-leaves { right: 0; top: 0; width: 190px; height: 230px; background: radial-gradient(circle at 60% 40%, #e9f2d8, #a9d065); }
  .art--town { left: 20px; top: 230px; width: 480px; height: 190px; background: linear-gradient(180deg, #dfecc0 0%, #8fc142 100%); }
  .cover-title { position: absolute; left: 48px; top: 560px; color: var(--white); font-size: 29px; font-weight: 700; }

  /* contents */
  .toc-title { position: absolute; left: 70px; top: 100px; color: var(--green-dark); font-size: 25px; font-weight: 700; }
  .toc-rule { position: absolute; left: 70px; top: 135px; width: 360px; height: 2px; background: var(--green); }
  .toc-list { position: absolute; left: 70px; top: 155px; width: 360px; list-style: none; }
  .toc-list li { display: flex; align-items: baseline; font-size: 11.5px; line-height: 21.5px; }
  .toc-list .leader { flex: 1; border-bottom: 1px dotted #888; margin: 0 5px; transform: translateY(-3px); }

  /* divider pages */
  .art--leaves-side { right: 0; top: 0; width: 230px; height: 707px; background: linear-gradient(180deg, rgba(255,255,255,.35), rgba(255,255,255,.05)); }
  .art--leaves-top { left: 0; top: 0; width: 500px; height: 270px; background: linear-gradient(180deg, rgba(255,255,255,.38), rgba(255,255,255,0)); }
  .vertical-title {
    position: absolute; left: 56px; bottom: 40px;
    writing-mode: vertical-rl; transform: rotate(180deg);
    color: var(--white); font-size: 36px; font-weight: 700;
  }
  .vertical-rule { position: absolute; left: 108px; width: 1px; background: rgba(255,255,255,.8); }

  /* product */
  .band-label { position: absolute; right: 40px; top: 18px; color: var(--white); font-size: 16px; font-weight: 700; }
  .product-title { position: absolute; left: 0; width: 500px; top: 100px; text-align: center; color: var(--green-dark); font-size: 24px; font-weight: 700; }
  .art--bottle { left: 60px; top: 150px; width: 380px; height: 250px; border: 1px solid #aaa; background: linear-gradient(180deg, #eef0f2 0%, #c8ccd0 100%); }
  .spec-tab { position: absolute; left: 60px; top: 400px; width: 150px; height: 26px; background: var(--green); color: var(--white); font-size: 14px; font-weight: 700; padding: 5px 10px; }
  .spec-table { position: absolute; left: 60px; top: 436px; border-collapse: collapse; font-size: 11px; }
  .spec-table th { text-align: left; font-weight: 700; width: 160px; padding: 3px 0; }
  .spec-table td { padding: 3px 0; }

  /* contact */
  .contact { position: absolute; left: 130px; top: 320px; color: var(--white); font-size: 10px; line-height: 14px; }
  .contact h3 { font-size: 12px; font-weight: 700; }
  .contact p { margin-bottom: 10px; }
</style>
</head>
<body>

<!-- Cover -->
<section class="sheet-slot">
  <div class="page page--light">
    <div class="art art--sky-leaves" role="img" aria-label="Falling paper-cut green and white leaves rising from a chimney"></div>
    <div class="art art--town" role="img" aria-label="Green illustrated factory, delivery truck and young trees on a hill"></div>
    <div class="brand"><span class="brand__dot"></span><span class="brand__name">Tidal Crate Supplies</span></div>
    <div class="brand__url">www.tidalcratesupplies.example</div>
    <svg class="band band--bottom" width="500" height="240" viewBox="0 0 500 240">
      <path d="M0 70 C150 20 320 40 500 0 L500 240 L0 240 Z" fill="var(--green)"/>
      <path d="M0 70 C150 20 320 40 500 0" fill="none" stroke="#dfe9b0" stroke-width="3"/>
    </svg>
    <div class="cover-title">Packaging Brochure</div>
  </div>
</section>

<!-- Table of contents -->
<section class="sheet-slot">
  <div class="page page--light">
    <svg class="band band--top" width="500" height="90" viewBox="0 0 500 90">
      <path d="M0 0 L500 0 L500 20 C330 30 180 60 0 80 Z" fill="var(--green)"/>
      <path d="M0 86 C180 66 330 36 500 28" fill="none" stroke="var(--green-light)" stroke-width="2"/>
    </svg>
    <h2 class="toc-title">Table of Content</h2>
    <div class="toc-rule"></div>
    <ul class="toc-list">
      <li>Powders Packaging<span class="leader"></span>1</li>
      <li>Liquids Packaging<span class="leader"></span>5</li>
      <li>Syrups Packaging<span class="leader"></span>7</li>
      <li>Dressings Packaging<span class="leader"></span>9</li>
      <li>Condiments Packaging<span class="leader"></span>12</li>
      <li>Sauces Packaging<span class="leader"></span>15</li>
      <li>Spreads Packaging<span class="leader"></span>20</li>
      <li>Spices Packaging<span class="leader"></span>25</li>
      <li>Cereals Packaging<span class="leader"></span>30</li>
      <li>Nuts Packaging<span class="leader"></span>35</li>
      <li>Extracts Packaging<span class="leader"></span>42</li>
      <li>Candy Packaging<span class="leader"></span>50</li>
      <li>Aluminum printed boxes<span class="leader"></span>52</li>
      <li>Dried Fruit (pouches)<span class="leader"></span>55</li>
      <li>Coffee Packaging<span class="leader"></span>60</li>
      <li>Pill jars<span class="leader"></span>62</li>
      <li>Supplement jars<span class="leader"></span>65</li>
    </ul>
    <svg class="band band--bottom" width="500" height="110" viewBox="0 0 500 110">
      <path d="M0 30 C180 10 330 20 500 0 L500 110 L0 110 Z" fill="var(--green)"/>
      <path d="M0 22 C180 2 330 12 500 -6" fill="none" stroke="var(--green-light)" stroke-width="2"/>
    </svg>
    <div class="folio">01</div>
  </div>
</section>

<!-- Category divider -->
<section class="sheet-slot">
  <div class="page page--green">
    <div class="art art--leaves-side" role="img" aria-label="Paper-cut green and white leaves drifting down the page"></div>
    <div class="vertical-rule" style="top:300px;height:380px"></div>
    <div class="vertical-title">Syrups Bottle</div>
  </div>
</section>

<!-- Product page -->
<section class="sheet-slot">
  <div class="page page--light">
    <svg class="band band--top" width="500" height="90" viewBox="0 0 500 90">
      <path d="M0 80 C180 60 330 30 500 0 L500 0 L0 0 Z" fill="var(--cream-deep)"/>
      <path d="M120 60 C260 40 380 10 500 0 L500 50 C380 60 260 60 120 60 Z" fill="var(--green)"/>
      <path d="M0 86 C180 66 330 36 500 2" fill="none" stroke="var(--green-light)" stroke-width="2"/>
    </svg>
    <div class="band-label">Syrups Bottle</div>
    <h2 class="product-title">MARLIN 250 ml</h2>
    <div class="art art--bottle" role="img" aria-label="Photo of two clear PET syrup bottles"></div>
    <div class="spec-tab">Specifications</div>
    <table class="spec-table">
      <tr><th>Type of Material:</th><td>Pet Plastic</td></tr>
      <tr><th>Weight:</th><td>30z</td></tr>
      <tr><th>HxLxW:</th><td>23x50x90mm</td></tr>
      <tr><th>Closure:</th><td>25mm</td></tr>
      <tr><th>Volume:</th><td>250ml</td></tr>
    </table>
    <svg class="band band--bottom" width="500" height="110" viewBox="0 0 500 110">
      <path d="M0 30 C180 10 330 20 500 0 L500 110 L0 110 Z" fill="var(--green)"/>
      <path d="M0 22 C180 2 330 12 500 -6" fill="none" stroke="var(--green-light)" stroke-width="2"/>
    </svg>
    <div class="folio">01</div>
  </div>
</section>

<!-- Contact -->
<section class="sheet-slot">
  <div class="page page--green">
    <div class="art art--leaves-top" role="img" aria-label="Paper-cut green and white leaves scattered across the top"></div>
    <div class="vertical-rule" style="top:300px;height:390px"></div>
    <div class="vertical-title">Contact us</div>
    <div class="contact">
      <h3>Production</h3>
      <p>Tidal Crate Supplies (Germany)</p>
      <p>Hafenweg 14<br>20457 Hamburg<br>Germany</p>
      <p>Tel: +49 (0)40 555 0142</p>
      <p>General: info@tidalcratesupplies.example<br>Jobs: jobs@tidalcratesupplies.example</p>
      <h3>Sales &amp; Fulfillment</h3>
      <p>Tidal Crate Supplies (The Netherlands)</p>
      <p>Dockstraat 8<br>1011 AB Harbourtown<br>The Netherlands</p>
      <p>Tel: +31 (0)20 555 0188</p>
      <p>Sales: sales@tidalcratesupplies.example<br>Fulfillment: orders@tidalcratesupplies.example</p>
    </div>
  </div>
</section>

</body>
</html>
```